Stationary/business card design for Harborline Building Partners
Harborline Building Partners
Stationary/business card design for Harborline Building Partners - Consulting
Creative Brief
Use specific fonts
Up to designer. Can be different from logo if that looks good.
Simple
Clara T Revanski
Director - Business Development & Support
3870 Wexmoor Avenue - Suite 2C Rochester, NY 14618
clara.revanski@hbpworkline.com
www.HBPworkline.com
The back of the business card will have some of what we do on there, for example: GIS, Drafting, Master Data. I haven't written that up yet.

```html
<!DOCTYPE html>
<html lang="en">
<head>
<meta charset="utf-8">
<title>Harborline Building Partners – Business Card</title>
<link href="https://fonts.googleapis.com/css2?family=Cinzel:wght@400;600&display=swap" rel="stylesheet">
<style>
  :root {
    --backdrop: #e6e4e0;
    --card: #ffffff;
    --brand-green: #1fae3c;
    --band-green: #22b33f;
    --rule-dark: #2b2f2c;
    --ink: #4a4d4b;
    --ink-soft: #6b6e6c;
    --white: #ffffff;
  }
  * { box-sizing: border-box; margin: 0; padding: 0; }
  html, body {
    width: 1200px; height: 914px; overflow: hidden;
    background: var(--backdrop);
    font-family: "Cinzel", "Times New Roman", serif;
  }
  .canvas {
    position: relative; width: 1200px; height: 914px;
    display: flex; align-items: center; justify-content: center;
  }
  .business-card {
    position: relative; width: 1050px; height: 600px;
    background: var(--card);
    box-shadow: 0 6px 24px rgba(0,0,0,0.12);
  }
  .brand {
    position: absolute; top: 170px; left: 330px;
    display: flex; align-items: center; gap: 22px;
  }
  .brand-mark {
    width: 26px; height: 26px; background: var(--brand-green);
  }
  .brand-name {
    font-size: 40px; font-weight: 600; letter-spacing: 1px;
    color: var(--brand-green); text-transform: uppercase;
    line-height: 1;
  }
  .identity-band {
    position: absolute; left: 0; right: 0; top: 300px;
    border-top: 5px solid var(--rule-dark);
    border-bottom: 5px solid var(--rule-dark);
  }
  .identity-band-fill {
    background: var(--band-green); height: 62px;
    margin: 4px 0;
    display: flex; align-items: center; padding-left: 150px;
    color: var(--white); font-size: 19px; letter-spacing: 1.5px;
    text-transform: uppercase;
  }
  .identity-name { font-weight: 600; }
  .identity-divider { margin: 0 14px; opacity: 0.85; }
  .contact {
    position: absolute; left: 28px; top: 405px; right: 28px;
    color: var(--ink); font-size: 17px; letter-spacing: 0.6px;
  }
  .contact-line {
    display: flex; align-items: center; flex-wrap: nowrap;
    white-space: nowrap; margin-bottom: 14px;
  }
  .contact-item { display: inline-flex; align-items: center; margin-right: 18px; }
  .contact-icon { width: 16px; height: 16px; margin-right: 6px; flex: none; }
</style>
</head>
<body>
<div class="canvas">
  <section class="business-card" aria-label="Business card front">
    <div class="brand">
      <span class="brand-mark"></span>
      <span class="brand-name">Harborline Building Partners</span>
    </div>

    <div class="identity-band">
      <div class="identity-band-fill">
        <span class="identity-name">Clara T Revanski</span>
        <span class="identity-divider">|</span>
        <span class="identity-title">Director - Business Development &amp; Support</span>
      </div>
    </div>

    <div class="contact">
      <div class="contact-line">
        <span class="contact-item">
          <svg class="contact-icon" viewBox="0 0 16 16"><circle cx="8" cy="8" r="8" fill="#1fae3c"/><path d="M8 3.5a2.8 2.8 0 0 0-2.8 2.8c0 2.1 2.8 5.2 2.8 5.2s2.8-3.1 2.8-5.2A2.8 2.8 0 0 0 8 3.5zm0 3.9a1.1 1.1 0 1 1 0-2.2 1.1 1.1 0 0 1 0 2.2z" fill="#fff"/></svg>
          3870 Wexmoor Avenue - Suite 2C Rochester, NY 14618
        </span>
        <span class="contact-item">
          <svg class="contact-icon" viewBox="0 0 16 16"><circle cx="8" cy="8" r="8" fill="#1fae3c"/><path d="M5.4 4.2l1.3-.4.9 2-1 .8a5 5 0 0 0 2.6 2.6l.8-1 2 .9-.4 1.3c-.2.5-.7.7-1.2.6A7 7 0 0 1 4.8 5.4c-.1-.5.1-1 .6-1.2z" fill="#fff"/></svg>
          585-410-2286
        </span>
        <span class="contact-item">
          <svg class="contact-icon" viewBox="0 0 16 16"><circle cx="8" cy="8" r="8" fill="#1fae3c"/><path d="M5.4 4.2l1.3-.4.9 2-1 .8a5 5 0 0 0 2.6 2.6l.8-1 2 .9-.4 1.3c-.2.5-.7.7-1.2.6A7 7 0 0 1 4.8 5.4c-.1-.5.1-1 .6-1.2z" fill="#fff"/></svg>
          585-447-3061
        </span>
      </div>
      <div class="contact-line">
        <span class="contact-item">
          <svg class="contact-icon" viewBox="0 0 16 16"><circle cx="8" cy="8" r="8" fill="#1fae3c"/><path d="M5.4 4.2l1.3-.4.9 2-1 .8a5 5 0 0 0 2.6 2.6l.8-1 2 .9-.4 1.3c-.2.5-.7.7-1.2.6A7 7 0 0 1 4.8 5.4c-.1-.5.1-1 .6-1.2z" fill="#fff"/></svg>
          585-410-2286
        </span>
        <span class="contact-item">
          <svg class="contact-icon" viewBox="0 0 16 16"><circle cx="8" cy="8" r="8" fill="#1fae3c"/><rect x="4" y="5" width="8" height="6" rx="0.8" fill="#fff"/><path d="M4.3 5.4L8 8.3l3.7-2.9" stroke="#1fae3c" stroke-width="0.9" fill="none"/></svg>
          clara.revanski@hbpworkline.com
        </span>
        <span class="contact-item">
          <svg class="contact-icon" viewBox="0 0 16 16"><circle cx="8" cy="8" r="8" fill="#1fae3c"/><circle cx="8" cy="8" r="4" fill="none" stroke="#fff" stroke-width="1"/><path d="M4 8h8M8 4c-1.6 1.2-1.6 6.8 0 8M8 4c1.6 1.2 1.6 6.8 0 8" stroke="#fff" stroke-width="0.9" fill="none"/></svg>
          www.HBPworkline.com
        </span>
      </div>
    </div>
  </section>
</div>
</body>
</html>
```